LumaWireHub full website re-design

I'm looking for a current, cool new design of my website, lumawirehub-example.com. We sell fiber optic cables and accessories. It hasn't been changed for over 10 years. I would like fresh ideas, not excessive pictures of cables. It has to be easy to navigate because we have over 5k products that we sell. The platform that our site is built on is Prestashop. I've attached many of our popular brands as well as some of our products so you can get an idea of what we sell. I also encourage you to go to our current website to see everything we offer. We are a high end brand and I want to give that impression. The winning designer will likely have ongoing work in the future because we will be making changes and additions to our site. Prestashop experience preferred! Be creative as you want. I would like banner images across the top as well.

Target Market(s)

Men 20-50

Industry/Entity Type

Technology

Coding

Coded - Design and coding required

Number of Pages Required

5+ page

Requirements
Must have
• https://www.videohost-example.com/watch?v=Qm7TzRb2pXo
Should not have
• cartoons

```html
<!DOCTYPE html>
<html lang="en">
<head>
<meta charset="utf-8">
<title>LumaWireHub — Fiber Optic Cables</title>
<link href="https://fonts.googleapis.com/css2?family=Poppins:wght@400;500;600;700&family=Syncopate:wght@700&display=swap" rel="stylesheet">
<style>
:root{
  --maroon:#8b1538;
  --maroon-dark:#6f0f2c;
  --nav-grey:#6c6c70;
  --dark-grey:#5e5f63;
  --text:#3d3d40;
  --muted:#7a7a7e;
  --light:#f3f3f3;
  --line:#e2e2e2;
  --white:#fff;
  --star:#f2b01e;
}
*{box-sizing:border-box;margin:0;padding:0}
html,body{width:1200px;height:4633px;overflow:hidden}
body{position:relative;background:var(--white);font-family:"Poppins",sans-serif;color:var(--text)}
a{color:inherit;text-decoration:none}
.abs{position:absolute}
.display{font-family:"Syncopate",sans-serif;font-weight:700;text-transform:uppercase}

/* header */
.brand{left:88px;top:26px;display:flex;align-items:center;gap:10px;font-size:26px;font-weight:600;color:var(--maroon)}
.brand-dot{width:30px;height:30px;border-radius:50%;border:3px solid var(--maroon)}
.search{left:459px;top:29px;width:302px;height:36px;border:1px solid #cfcfcf;display:flex;align-items:center;padding-left:22px;font-size:11px;color:#999}
.search svg{position:absolute;right:0;top:0;width:44px;height:34px;border-left:1px solid #cfcfcf;padding:9px 13px}
.call{left:806px;top:27px;display:flex;gap:8px;align-items:flex-start}
.call small{display:block;font-size:9px;color:#888;letter-spacing:.5px}
.call b{font-size:14px;font-weight:500;color:var(--text)}
.hicons{left:992px;top:30px;display:flex;gap:20px;align-items:center}
.hicons svg{width:24px;height:28px}

.navbar{left:0;top:94px;width:1200px;height:48px;background:var(--nav-grey)}
.cat-btn{left:90px;top:0;width:254px;height:48px;background:var(--maroon);color:#fff;font-size:13px;font-weight:500;display:flex;align-items:center;justify-content:center;gap:10px}
.nav-links{left:450px;top:0;height:48px;display:flex}
.nav-links a{color:#fff;font-size:13px;font-weight:500;padding:0 26px;line-height:48px;border-right:1px solid rgba(255,255,255,.3)}

/* hero */
.hero{left:0;top:142px;width:1200px;height:652px;background:linear-gradient(#ececec,#f6f6f6 40%,#e9e9e9)}
.hero-photo{left:0;top:320px;width:1200px;height:332px;background:linear-gradient(100deg,#f2d23a 0%,#f0b832 25%,#ee8a2c 50%,#3d6fd0 62%,#e9e4d8 75%,#2b2b2b 92%,#e9e9e9 100%);opacity:.85}
.hero h1{left:0;top:100px;width:1200px;text-align:center;font-size:46px;line-height:51px;color:#5a5a5e;letter-spacing:2px}
.hero p{left:0;top:208px;width:1200px;text-align:center;font-size:16px;color:#333}
.btn-maroon{background:var(--maroon);color:#fff;font-weight:600;font-size:14px;display:flex;align-items:center;justify-content:center}
.hero .btn-maroon{left:527px;top:256px;width:144px;height:43px}
.slide-arrow{top:292px;width:30px;height:70px;background:#b3b3b3;color:#fff;display:flex;align-items:center;justify-content:center;font-size:14px}

/* section titles */
.sec-title{left:0;width:1200px;text-align:center;font-size:34px;color:#555558;letter-spacing:1px}

.card{background:#fff;box-shadow:0 2px 10px rgba(0,0,0,.12)}
.cat-card{top:935px;width:247px;height:301px;text-align:center}
.cat-card .ph{margin:8px;height:186px}
.cat-card h3{font-size:13px;font-weight:500;color:#555;line-height:17px;margin-top:30px;letter-spacing:.5px}
.cat-card a{display:inline-block;margin-top:17px;font-size:11px;font-weight:600;color:var(--maroon);border-bottom:1px solid var(--maroon)}
.pager{display:flex;gap:6px}
.pager span{width:30px;height:30px;background:#ececec;display:flex;align-items:center;justify-content:center;font-size:12px;color:#555}

/* clearance */
.clearance{left:0;top:1403px;width:1200px;height:447px;background:var(--maroon)}
.clearance .big{left:112px;top:92px;font-size:90px;line-height:90px;color:#fff}
.clearance .mid{left:112px;top:188px;font-size:47px;color:#fff}
.clearance p{left:116px;top:256px;font-size:24px;color:#fff;letter-spacing:.5px}
.btn-white{left:117px;top:309px;width:144px;height:45px;background:#fff;color:#333;font-size:14px;font-weight:600;display:flex;align-items:center;justify-content:center}
.perk{top:94px;width:219px;height:260px;background:#fff;text-align:center;box-shadow:0 6px 20px rgba(0,0,0,.25)}
.perk .ic{width:112px;height:112px;border-radius:50%;background:#6c6c70;margin:38px auto 0;display:flex;align-items:center;justify-content:center}
.perk p{font-size:13px;color:#555;line-height:19px;margin-top:18px;padding:0 20px}

/* products */
.prod{top:2004px;width:244px;height:342px;text-align:center}
.prod .ph{height:168px;margin:0}
.prod .stars{margin-top:16px;color:var(--star);font-size:13px;letter-spacing:3px}
.prod h3{font-size:12px;font-weight:400;color:#555;line-height:16px;margin-top:6px;padding:0 16px}
.prod .price{font-size:18px;font-weight:600;color:var(--maroon);margin-top:8px}
.prod .add{margin:8px auto 0;width:200px;height:40px;background:#e8e8e8;font-size:12px;font-weight:600;color:#555;display:flex;align-items:center;justify-content:center}

/* video */
.pattern-band{left:0;top:2938px;width:1200px;height:714px;background:#f1f1f1}
.video-sub{left:0;top:2548px;width:1200px;text-align:center;font-size:11px;color:#444}
.video{left:219px;top:2598px;width:761px;height:430px;background:#4a4a4d;display:block;z-index:2}
.video .cable{position:absolute;left:120px;top:60px;width:520px;height:290px;background:radial-gradient(ellipse at 40% 45%,#7fd8c6,#4fae9f 40%,rgba(74,74,77,0) 72%)}
.video .headline{position:absolute;right:26px;top:26px;color:#fff;font-size:28px;font-weight:600;line-height:30px;text-align:right}
.video .headline span{font-size:22px;font-weight:400}
.video .headline b{font-size:54px;color:#7fe0cf;font-weight:700}
.video .play{position:absolute;left:350px;top:185px;width:64px;height:64px;border-radius:50%;background:#222;display:flex;align-items:center;justify-content:center}
.deco-photo{border-radius:4px;z-index:1}

.feature{top:3132px;width:244px;height:331px;text-align:center;z-index:2}
.feature.active{background:#fff;box-shadow:0 4px 20px rgba(0,0,0,.1)}
.feature .ic{width:96px;height:96px;border-radius:50%;background:#6c6c70;margin:31px auto 0;display:flex;align-items:center;justify-content:center}
.feature.active .ic{background:var(--maroon)}
.feature h3{font-size:15px;font-weight:600;color:#555;line-height:20px;margin-top:22px}
.feature p{font-size:11px;color:#555;line-height:20px;margin-top:12px;padding:0 18px}
.feature .arrow{margin-top:16px;font-size:16px;color:#555}

.brands{left:0;top:3722px;width:1200px;height:60px}
.brand-name{top:12px;width:200px;text-align:center;font-size:24px;font-weight:600;color:#3a3a3d}

/* newsletter */
.newsletter{left:0;top:3900px;width:1200px;height:216px;background:var(--dark-grey)}
.newsletter h2{left:86px;top:72px;font-size:34px;line-height:40px;color:#fff}
.nl-label{top:70px;font-size:12px;font-weight:600;color:#fff}
.nl-input{top:85px;width:218px;height:51px;background:#fff;font-size:13px;color:#888;padding-left:16px;display:flex;align-items:center}
.newsletter .btn-maroon{left:959px;top:85px;width:151px;height:51px}

/* footer */
.f-brand{left:86px;top:4250px;display:flex;align-items:center;gap:10px;font-size:28px;font-weight:600;color:var(--maroon)}
.f-col{top:4188px}
.f-col h4{font-size:14px;font-weight:600;color:#444;margin-bottom:20px}
.f-col li{list-style:none;font-size:13px;color:#555;line-height:27px}
.f-col .c-label{font-size:11px;font-weight:600;color:#444;margin-top:10px}
.f-col .c-text{font-size:13px;color:#555;line-height:20px}
.f-rule{left:0;top:4492px;width:1200px;height:1px;background:var(--line)}
.buy{left:90px;top:4512px;display:flex;gap:8px;align-items:center}
.buy small{display:block;font-size:11px;color:#555}
.buy b{font-size:17px;font-weight:600;color:var(--maroon)}
.socials{left:497px;top:4522px;display:flex;gap:17px}
.socials span{width:28px;height:28px;border-radius:50%;background:#e4e4e4}
.payments{left:962px;top:4524px;display:flex;gap:6px}
.payments span{width:44px;height:26px;border-radius:3px;background:#e0e0e6}
.payments span:nth-child(2){background:#d6d6d6}
.payments span:nth-child(3){background:#cfdcea}
.copy{left:0;top:4598px;width:1200px;text-align:center;font-size:13px;color:#444}
.chat{left:1122px;top:4460px;width:60px;height:60px;border-radius:50%;background:var(--maroon);display:flex;align-items:center;justify-content:center}
</style>
</head>
<body>

<header>
  <a class="abs brand" href="#"><span class="brand-dot"></span>LumaWireHub</a>
  <div class="abs search">What can we help you find?
    <svg viewBox="0 0 18 18"><circle cx="7.5" cy="7.5" r="6" fill="none" stroke="#555" stroke-width="1.8"/><path d="M12 12l5 5" stroke="#555" stroke-width="1.8"/></svg>
  </div>
  <div class="abs call">
    <svg width="16" height="16" viewBox="0 0 24 24"><path d="M6.6 10.8a15 15 0 006.6 6.6l2.2-2.2c.3-.3.7-.4 1-.2 1.1.4 2.3.6 3.6.6.6 0 1 .4 1 1V20c0 .6-.4 1-1 1C10.6 21 3 13.4 3 4c0-.6.4-1 1-1h3.5c.6 0 1 .4 1 1 0 1.3.2 2.5.6 3.6.1.3 0 .7-.2 1z" fill="var(--maroon)"/></svg>
    <div><small>CALL US</small><b>866-555-0142</b></div>
  </div>
  <div class="abs hicons">
    <svg viewBox="0 0 24 24"><rect x="5" y="11" width="14" height="10" rx="1" fill="#555"/><path d="M8 11V8a4 4 0 018 0v3" fill="none" stroke="#555" stroke-width="2"/></svg>
    <svg viewBox="0 0 24 24"><circle cx="12" cy="8" r="4.5" fill="#555"/><path d="M3.5 22a8.5 8 0 0117 0z" fill="#555"/></svg>
    <svg viewBox="0 0 30 28"><path d="M1 3h5l4 15h14l3-10H8" fill="none" stroke="#555" stroke-width="2"/><circle cx="12" cy="23" r="2" fill="#555"/><circle cx="22" cy="23" r="2" fill="#555"/><circle cx="26" cy="4" r="4" fill="var(--maroon)"/></svg>
  </div>
</header>

<nav class="abs navbar">
  <a class="abs cat-btn" href="#">
    <svg width="20" height="14" viewBox="0 0 20 14"><path d="M0 1h20M4 7h16M0 13h20" stroke="#fff" stroke-width="2"/></svg>SHOP BY CATEGORIES
  </a>
  <div class="abs nav-links">
    <a href="#">HOME</a><a href="#">30 MIN QUOTE</a><a href="#">CUSTOM CABLECUSTOM</a><a href="#">CABLEPURCHASING</a>
  </div>
</nav>

<section class="abs hero">
  <div class="abs hero-photo" role="img" aria-label="Coiled yellow, orange and black fiber patch cables with connectors"></div>
  <h1 class="abs display">Beauty is in the eye<br>of the installer</h1>
  <p class="abs">Avoid The Slack With Our Custom, Exact Length Cables</p>
  <a class="abs btn-maroon" href="#">SHOP NOW</a>
  <span class="abs slide-arrow" style="left:0">‹</span>
  <span class="abs slide-arrow" style="right:0">›</span>
</section>

<h2 class="abs sec-title display" style="top:872px">Categories</h2>
<article class="abs card cat-card" style="left:90px"><div class="ph" role="img" aria-label="Aqua duplex fiber connector" style="background:linear-gradient(135deg,#f6f6f6,#bfe3dc 55%,#f2f2f2)"></div><h3>FLEXTURN FIBER<br>PATCH CABLES</h3><a href="#">SHOP NOW</a></article>
<article class="abs card cat-card" style="left:347px"><div class="ph" role="img" aria-label="Blue singlemode fiber connector" style="background:linear-gradient(135deg,#f6f6f6,#9cb8e6 55%,#f2f2f2)"></div><h3>TAA OS2 SINGLEMODE<br>FIBER CABLES</h3><a href="#">SHOP NOW</a></article>
<article class="abs card cat-card" style="left:606px"><div class="ph" role="img" aria-label="Beige multimode fiber connector" style="background:linear-gradient(135deg,#f6f6f6,#d8cdc6 55%,#f2f2f2)"></div><h3>TAA OM1 MULTIMODE<br>FIBER CABLES</h3><a href="#">SHOP NOW</a></article>
<article class="abs card cat-card" style="left:863px"><div class="ph" role="img" aria-label="Beige multimode fiber connector" style="background:linear-gradient(135deg,#f6f6f6,#d6cdc8 55%,#f2f2f2)"></div><h3>TAA OM4 MULTIMODE<br>FIBER CABLES</h3><a href="#">SHOP NOW</a></article>
<div class="abs pager" style="left:566px;top:1281px"><span>‹</span><span>›</span></div>

<section class="abs clearance">
  <div class="abs big display">Huge</div>
  <div class="abs mid display">Clearance</div>
  <p class="abs">A WIDE SELECTIONS OF ITEMS</p>
  <a class="abs btn-white" href="#">SHOP NOW</a>
  <div class="abs perk" style="left:631px">
    <div class="ic"><svg width="56" height="56" viewBox="0 0 24 24"><path d="M12 2l9 4v2H3V6z M5 9h2v8H5z M11 9h2v8h-2z M17 9h2v8h-2z M3 18h18v3H3z" fill="#fff"/></svg></div>
    <p>Military *Government* Education Preferred Pricing</p>
  </div>
  <div class="abs perk" style="left:862px">
    <div class="ic"><svg width="56" height="56" viewBox="0 0 24 24"><path d="M4 20L14 10M15 3a4 4 0 014 5l-3 1-2-2 1-3zM20 20L9 9M4 4l3 1 1 3-3-1z" stroke="#fff" stroke-width="2" fill="none" stroke-linecap="round"/></svg></div>
    <p>Cable configuration Instant Quote</p>
  </div>
</section>

<h2 class="abs sec-title display" style="top:1940px">Our Products</h2>
<article class="abs card prod" style="left:90px"><div class="ph" role="img" aria-label="OM3 LC duplex patch cable" style="background:linear-gradient(150deg,#fff 30%,#cdeee6 60%,#fff)"></div><div class="stars">★★★★★</div><h3>OM3 LC LC Duplex Fiber Patch Cable 10Gb Multimode 50/125</h3><div class="price">$9.95</div><a class="add" href="#">ADD TO CART</a></article>
<article class="abs card prod" style="left:349px"><div class="ph" role="img" aria-label="OS2 LC SC singlemode patch cable" style="background:linear-gradient(150deg,#fff 30%,#b3c8ee 55%,#f6e79a 75%,#fff)"></div><div class="stars">★★★★★</div><h3>OS2 LC SC Plenum Duplex Fiber Patch Cable 9/125 Singlemode</h3><div class="price">$24.19</div><a class="add" href="#">ADD TO CART</a></article>
<article class="abs card prod" style="left:607px"><div class="ph" role="img" aria-label="OM1 LC ST multimode patch cable" style="background:linear-gradient(150deg,#fff 30%,#9a9a9a 55%,#f6c79a 75%,#fff)"></div><div class="stars">★★★★★</div><h3>OM1 LC ST Plenum Duplex Fiber Patch Cable 62.5/125 Multimode</h3><div class="price">$29.00</div><a class="add" href="#">ADD TO CART</a></article>
<article class="abs card prod" style="left:866px"><div class="ph" role="img" aria-label="OM3 LC ST multimode patch cable" style="background:linear-gradient(150deg,#fff 30%,#9a9a9a 55%,#cdeee6 75%,#fff)"></div><div class="stars">★★★★★</div><h3>M3 LC ST Plenum Duplex Fiber Patch Cable 10G Multimode 50/125</h3><div class="price">$27.95</div><a class="add" href="#">ADD TO CART</a></article>
<div class="abs pager" style="left:559px;top:2399px"><span>‹</span><span>›</span></div>

<div class="abs pattern-band"></div>
<h2 class="abs sec-title display" style="top:2502px">LWH Video</h2>
<p class="abs video-sub">LumaWireHub - FlexTurn LC LC Fiber Patch Cables | OS2 SMF &amp; OM4 MMF Duplex Jumpers</p>
<a class="abs video" href="https://www.videohost-example.com/watch?v=Qm7TzRb2pXo">
  <div class="cable" role="img" aria-label="Aqua duplex connector with a cable bent at ninety degrees"></div>
  <div class="headline">Bend and maintain<br><span>at any angle to </span><b>90°</b></div>
  <div class="play"><svg width="20" height="22" viewBox="0 0 20 22"><path d="M3 2l15 9-15 9z" fill="#fff"/></svg></div>
</a>
<div class="abs deco-photo" role="img" aria-label="Black ST connectors on an orange cable" style="left:1060px;top:2860px;width:140px;height:180px;background:linear-gradient(160deg,#ee8a2c,#555 60%,rgba(241,241,241,0))"></div>
<div class="abs deco-photo" role="img" aria-label="Yellow fiber cable with black ST connectors" style="left:0;top:3340px;width:195px;height:310px;background:linear-gradient(200deg,#f2d23a,#444 60%,rgba(241,241,241,0))"></div>

<article class="abs feature" style="left:211px">
  <div class="ic"><svg width="46" height="46" viewBox="0 0 24 24"><path d="M4 20c5-2 6-6 9-9l3-3M14 4l6 6-4 4-6-6z" stroke="#fff" stroke-width="1.8" fill="none"/></svg></div>
  <h3>Express Custom<br>Cables</h3>
  <p>LWH offers TAA Compliant and Made in the USA fiber optic cables. We can custom build any length and type of fiber you...</p>
  <div class="arrow">→</div>
</article>
<article class="abs feature active" style="left:479px">
  <div class="ic"><svg width="46" height="46" viewBox="0 0 24 24"><circle cx="12" cy="9" r="6" stroke="#fff" stroke-width="1.8" fill="none"/><path d="M8 14l-2 8 6-3 6 3-2-8" stroke="#fff" stroke-width="1.8" fill="none"/></svg></div>
  <h3>Lifetime<br>Warranty</h3>
  <p>We stand behind the craftsmanship of every fiber optic product we deliver. From Indoor / Outdoor, Single mode...</p>
  <div class="arrow">→</div>
</article>
<article class="abs feature" style="left:745px">
  <div class="ic"><svg width="50" height="46" viewBox="0 0 26 24"><path d="M1 6h15v11H1zM16 10h5l4 4v3h-9z" stroke="#fff" stroke-width="1.6" fill="none"/><circle cx="6" cy="19" r="2" fill="#fff"/><circle cx="20" cy="19" r="2" fill="#fff"/></svg></div>
  <h3>Free Ground<br>Shipping</h3>
  <p>Quality tested, securely packages, then shipped via Free parcel Ground to your door step complete with test results. Free...</p>
  <div class="arrow">→</div>
</article>

<section class="abs brands">
  <div class="abs brand-name" style="left:116px">IronClad Pro</div>
  <div class="abs brand-name" style="left:373px">SnugLine</div>
  <div class="abs brand-name" style="left:634px">FlexTurn</div>
  <div class="abs brand-name" style="left:871px">NextPlay</div>
</section>

<section class="abs newsletter">
  <h2 class="abs display">Sign up for<br>newsletter</h2>
  <label class="abs nl-label" style="left:495px">FIRST NAME*</label>
  <div class="abs nl-input" style="left:495px">Enter your name</div>
  <label class="abs nl-label" style="left:721px">EMAIL ADDRESS*</label>
  <div class="abs nl-input" style="left:721px">Enter your address</div>
  <a class="abs btn-maroon" href="#">YES, SEND IT!</a>
</section>

<footer>
  <a class="abs f-brand" href="#"><span class="brand-dot"></span>LumaWireHub</a>
  <div class="abs f-col" style="left:367px">
    <h4>SECURE SHOPPING</h4>
    <ul><li>Privacy Policy</li><li>Shipping Information</li><li>Terms and Conditions</li><li>Return Policy</li><li>Apply for Credit</li><li>Reviews</li><li>Visit Our Blog</li><li>Contact Us</li></ul>
  </div>
  <div class="abs f-col" style="left:642px">
    <h4>MY ACCOUNT</h4>
    <ul><li>Home</li><li>About Us</li><li>Reseller</li><li>Gov/Edu Buyers</li><li>Resellers</li></ul>
  </div>
  <div class="abs f-col" style="left:883px;width:240px">
    <h4>CONTACT INFO</h4>
    <div class="c-label">TOLL FREE</div><div class="c-text">Call us now: (866) 555-0142</div>
    <div class="c-label">EMAIL</div><div class="c-text">sales@lumawirehub-example.com</div>
    <div class="c-label">LOCATION</div><div class="c-text">LWH Sales Office | Warehouse , 420 Meridian Ave. Suite B | RIVERTON, CA 90210 - 118</div>
  </div>
  <div class="abs f-rule"></div>
  <div class="abs buy">
    <svg width="16" height="30" viewBox="0 0 16 30"><rect x="1" y="1" width="14" height="28" rx="2" fill="none" stroke="var(--maroon)" stroke-width="2"/><circle cx="8" cy="25" r="1.5" fill="var(--maroon)"/></svg>
    <div><small>Buy Online Or Call</small><b>(866) 555-0142</b></div>
  </div>
  <div class="abs socials" aria-label="Social links"><span></span><span></span><span></span><span></span><span></span></div>
  <div class="abs payments" aria-label="Accepted payment cards"><span></span><span></span><span></span></div>
  <p class="abs copy">Copyright © 2021 - LumaWireHub, Inc. All Right Reserved</p>
  <div class="abs chat"><svg width="30" height="28" viewBox="0 0 24 22"><path d="M2 2h20v14H8l-5 4v-4H2z" fill="#fff"/><circle cx="8" cy="9" r="1.3" fill="var(--maroon)"/><circle cx="12" cy="9" r="1.3" fill="var(--maroon)"/><circle cx="16" cy="9" r="1.3" fill="var(--maroon)"/></svg></div>
</footer>

</body>
</html>
```